Webdesign für Zahnarztpraxis
Zielgruppe
Zahnarztpraxis
Aufgabenstellung
- Klares und übersichtliches Desgin
- Nicht zu verspielt
- Informativ
- Leichte Naviagtion
- Das Design der alten Webseite soll NICHT kopiert werden
- Die Farben Blau und Grün aus dem Logo sollen sich wiederfinden
- Designbeispiele, die dem Kunden gefallen sind https://www.kolbe-nardini-zahnarztpraxis.de/ und https://www.pilotrick.de/

```html
<!DOCTYPE html>
<html lang="de">
<head>
<meta charset="utf-8">
<title>Lindenhof Dental – Praxis & Dentallabor</title>
<link href="https://fonts.googleapis.com/css2?family=Roboto:wght@400;500;700&display=swap" rel="stylesheet">
<style>
:root{
  --blue:#1d9ad6;
  --green:#6cb33f;
  --ink:#1e1e1e;
  --white:#ffffff;
}
*{margin:0;padding:0;box-sizing:border-box}
html,body{width:1200px;height:4980px;overflow:hidden;background:var(--white)}
body{position:relative;font-family:"Roboto",Arial,sans-serif;color:var(--ink)}
.abs{position:absolute}
.top-bar{left:0;top:0;width:1200px;height:12px;background:var(--blue)}
.brand{font-weight:700;color:var(--blue);display:flex;align-items:center;gap:12px;white-space:nowrap}
.brand-dot{width:34px;height:34px;border-radius:50%;background:var(--green);flex:none}
.brand-top{left:141px;top:34px;font-size:30px}
.main-nav{top:40px;left:560px;width:560px;display:flex;justify-content:space-between;font-size:14px;font-weight:700;color:var(--green)}
.hero-text{left:130px;top:240px;width:436px;text-align:center;color:var(--blue);font-weight:700;font-size:27px;line-height:50px}
.btn{left:176px;top:592px;width:302px;height:62px;border-radius:31px;background:var(--green);color:var(--white);font-size:38px;font-weight:700;display:flex;align-items:center;justify-content:center}
.photo{background:linear-gradient(160deg,#eef3f6,#c8d3dc 60%,#b9a99a)}
.hero-photo{left:573px;top:93px;width:514px;height:662px;border-radius:0 0 0 60px}
.rule{height:10px;background:var(--green)}
.section-title{left:0;width:1200px;text-align:center;color:var(--blue);font-weight:700;font-size:46px}
.service{display:flex;align-items:center;gap:8px;width:330px}
.service svg{width:92px;height:92px;flex:none}
.service span{font-size:20px;font-weight:700;line-height:24px;max-width:150px}
.lead{text-align:center;color:var(--blue);font-weight:700}
.lab-lead{left:120px;top:2210px;width:390px;font-size:46px;line-height:58px}
.lab-photo{left:538px;top:2154px;width:588px;height:383px;background:linear-gradient(135deg,#f4f6f7,#dfe4e6 55%,#c9b7a3)}
.team-lead{left:118px;top:2850px;width:372px;font-size:32px;line-height:39px}
.team-photo{left:500px;top:2811px;width:694px;height:362px;background:linear-gradient(90deg,#f3f4f5,#e4d3d0 35%,#b8bfd0 70%,#f1f1f2)}
.member{display:flex;gap:15px;width:440px}
.member .portrait{width:132px;height:195px;flex:none;background:linear-gradient(180deg,#b9c98a,#eef0ee 60%,#ffffff)}
.member .bio{font-size:10px;font-weight:700;line-height:12.5px;padding-top:22px}
.member .bio h4{font-size:10px;margin-bottom:14px}
.contact{left:0;width:1200px;text-align:center;font-size:19px;font-weight:500;line-height:23px;color:var(--green)}
.contact p{margin:0}
.contact .blue{color:var(--blue)}
.footer-box{left:435px;top:4776px;width:759px;height:204px;background:var(--blue)}
.footer-nav{left:535px;top:4862px;width:580px;display:flex;justify-content:space-between;font-size:14px;font-weight:700;color:var(--white)}
.brand-foot{left:110px;top:4850px;font-size:30px}
</style>
</head>
<body>
<svg width="0" height="0" style="position:absolute">
  <symbol id="tooth" viewBox="0 0 48 48">
    <path d="M14 6C8 6 5 11 6 18c1 7 4 10 5 18 1 6 2 9 4 9 3 0 3-11 9-13 6 2 6 13 9 13 2 0 3-3 4-9 1-8 4-11 5-18 1-7-2-12-8-12-4 0-6 3-10 3s-6-3-10-3z" fill="none" stroke="#1d9ad6" stroke-width="3" stroke-linejoin="round"/>
  </symbol>
</svg>

<div class="abs top-bar"></div>
<div class="abs brand brand-top"><span class="brand-dot"></span>Lindenhof Dental</div>
<nav class="abs main-nav"><span>Unsere Praxis</span><span>Leistungen</span><span>Praxislabor</span><span>Team</span><span>Kontakt</span></nav>

<div class="abs hero-text">Praxis &amp; Dentallabor in<br>Grünwalde.<br>Prävention und<br>Individualprophylaxe in jeder<br>Altersgruppe!<br>Zahnärztin spricht auch fließend<br>Englisch.</div>
<div class="abs btn">Leistungen</div>
<div class="abs photo hero-photo" role="img" aria-label="Foto: Zahnärztin behandelt einen jungen Patienten"></div>
<div class="abs rule" style="left:0;top:757px;width:1200px"></div>

<h2 class="abs section-title" style="top:808px">Leistungen</h2>

<div class="abs service" style="left:246px;top:941px"><svg viewBox="0 0 48 48"><use href="#tooth"/><circle cx="26" cy="24" r="8" fill="#fff" stroke="#6cb33f" stroke-width="3"/><path d="M32 30l8 8" stroke="#6cb33f" stroke-width="4" stroke-linecap="round"/></svg><span>Zahnärztliche Diagnostik</span></div>
<div class="abs service" style="left:635px;top:941px"><svg viewBox="0 0 48 48"><use href="#tooth"/></svg><span>Chirurgische Zahnheilkunde</span></div>

<div class="abs service" style="left:246px;top:1096px"><svg viewBox="0 0 48 48"><use href="#tooth"/><path d="M24 14l9 3v8c0 6-4 10-9 12-5-2-9-6-9-12v-8z" fill="none" stroke="#6cb33f" stroke-width="3"/></svg><span>Individualprophylaxe</span></div>
<div class="abs service" style="left:635px;top:1096px"><svg viewBox="0 0 48 48"><use href="#tooth"/><path d="M8 2l1.5 4 4 1.5-4 1.5L8 13l-1.5-4-4-1.5 4-1.5zM26 16l1.5 4 4 1.5-4 1.5-1.5 4-1.5-4-4-1.5 4-1.5z" fill="#6cb33f"/></svg><span>Ästhetische Zahnheilkunde</span></div>

<div class="abs service" style="left:246px;top:1251px"><svg viewBox="0 0 48 48"><use href="#tooth"/><path d="M18 30L38 8" stroke="#6cb33f" stroke-width="3" stroke-linecap="round"/><path d="M30 12l4 4M33 9l4 4M36 6l4 4" stroke="#6cb33f" stroke-width="2"/></svg><span>Professionelle Zahnreinigung</span></div>
<div class="abs service" style="left:635px;top:1251px"><svg viewBox="0 0 48 48"><use href="#tooth"/><circle cx="36" cy="11" r="9" fill="#6cb33f"/><path d="M36 6v10M31 11h10" stroke="#fff" stroke-width="3"/></svg><span>Ganzheitliche Zahnheilkunde</span></div>

<div class="abs service" style="left:246px;top:1405px"><svg viewBox="0 0 48 48"><use href="#tooth"/><path d="M14 24l7 7 16-16" fill="none" stroke="#6cb33f" stroke-width="4" stroke-linecap="round" stroke-linejoin="round"/></svg><span>Konservierende Zahnheilkunde</span></div>
<div class="abs service" style="left:635px;top:1405px"><svg viewBox="0 0 48 48"><use href="#tooth"/><circle cx="19" cy="18" r="1.8" fill="#6cb33f"/><circle cx="29" cy="18" r="1.8" fill="#6cb33f"/><path d="M18 24q6 6 12 0" fill="none" stroke="#6cb33f" stroke-width="2.5" stroke-linecap="round"/></svg><span>Kinderzahnheilkunde</span></div>

<div class="abs service" style="left:246px;top:1560px"><svg viewBox="0 0 48 48"><path d="M12 6c-5 0-7 4-6 8 1 3 5 5 18 5s17-2 18-5c1-4-1-8-6-8-4 0-6 2-12 2S16 6 12 6z" fill="none" stroke="#1d9ad6" stroke-width="3"/><path d="M18 24h12M19 30h10M20 36h8M21 42h6" stroke="#6cb33f" stroke-width="3" stroke-linecap="round"/></svg><span>Zahnärztliche Prothetik</span></div>
<div class="abs service" style="left:635px;top:1560px"><svg viewBox="0 0 48 48"><use href="#tooth"/><g transform="translate(10 6) scale(.8)"><use href="#tooth"/></g></svg><span>Bioverträglicher Zahnersatz</span></div>

<div class="abs service" style="left:246px;top:1715px"><svg viewBox="0 0 48 48"><use href="#tooth"/><path d="M9 20h30" stroke="#6cb33f" stroke-width="2"/><rect x="13" y="17" width="6" height="6" fill="#6cb33f"/><rect x="29" y="17" width="6" height="6" fill="#6cb33f"/></svg><span>Kieferorthopädie</span></div>

<div class="abs rule" style="left:4px;top:1875px;width:1196px"></div>

<h2 class="abs section-title" style="top:2017px;left:-40px">Praxislabor</h2>
<div class="abs lead lab-lead">Unsere Praxis verfügt über ein eigenes Praxislabor.</div>
<div class="abs photo lab-photo" role="img" aria-label="Foto: heller Behandlungsraum mit Behandlungsstuhl und Schränken"></div>
<div class="abs rule" style="left:10px;top:2537px;width:1190px"></div>

<h2 class="abs section-title" style="top:2679px;left:15px">Team</h2>
<div class="abs photo team-photo" role="img" aria-label="Gruppenfoto des Praxisteams"></div>
<div class="abs lead team-lead">kompetent, herzlich und darauf fokussiert, Ihre Zahngesundheit bestmöglich zu unterstützen.</div>

<div class="abs member" style="left:143px;top:3228px"><div class="portrait" role="img" aria-label="Porträt der Zahnärztin"></div><div class="bio"><h4>Zahnärztin Sabine Hartung</h4>-2004 Studienabschluss<br>- von 2005 bis 2015 in England tätig<br>- Behandlungsschwerpunkte: ästhetische,<br>&nbsp;&nbsp;preventive Zahnheilkunde<br>&nbsp;&nbsp;Zahnaufhellung /Bleachingfeste,<br>&nbsp;&nbsp;kosmetische Zahnspangen<br>- Spezialgebiete: Wurzelkanalbehandlung<br>&nbsp;&nbsp;Endodontie,<br>&nbsp;&nbsp;seit 2009 Zahnfehlstellungskorrektur:<br>&nbsp;&nbsp;zertifizierte Aligner-Anbieterin</div></div>
<div class="abs member" style="left:611px;top:3228px"><div class="portrait" role="img" aria-label="Porträt der Zahnärztin"></div><div class="bio"><h4>Zahnärztin Sabine Hartung</h4>-2004 Studienabschluss<br>- von 2005 bis 2015 in England tätig<br>- Behandlungsschwerpunkte: ästhetische,<br>&nbsp;&nbsp;preventive Zahnheilkunde<br>&nbsp;&nbsp;Zahnaufhellung /Bleachingfeste,<br>&nbsp;&nbsp;kosmetische Zahnspangen<br>- Spezialgebiete: Wurzelkanalbehandlung<br>&nbsp;&nbsp;Endodontie,<br>&nbsp;&nbsp;seit 2009 Zahnfehlstellungskorrektur:<br>&nbsp;&nbsp;zertifizierte Aligner-Anbieterin</div></div>

<div class="abs member" style="left:143px;top:3446px"><div class="portrait" role="img" aria-label="Porträt der Zahntechnikerin"></div><div class="bio"><h4>Zahntechnikerin Nadine Kessler</h4>- 2002 Abschluss der Ausbildung<br>- seit 2011 in unserer Praxis<br>- Spezialgebiete: Kronen- und Brückentechnik<br>&nbsp;&nbsp;&nbsp;&nbsp;&nbsp;&nbsp;&nbsp;&nbsp;&nbsp;&nbsp;&nbsp;&nbsp;Metallkeramik- und Presskeramik<br>&nbsp;&nbsp;&nbsp;&nbsp;&nbsp;&nbsp;&nbsp;&nbsp;&nbsp;&nbsp;&nbsp;&nbsp;Teleskoptechnik<br>&nbsp;&nbsp;&nbsp;&nbsp;&nbsp;&nbsp;&nbsp;&nbsp;&nbsp;&nbsp;&nbsp;&nbsp;Totalprothetik<br>&nbsp;&nbsp;&nbsp;&nbsp;&nbsp;&nbsp;&nbsp;&nbsp;&nbsp;&nbsp;&nbsp;&nbsp;Vollkeramik - metallfrei</div></div>
<div class="abs member" style="left:611px;top:3446px"><div class="portrait" role="img" aria-label="Porträt der Zahnärztin"></div><div class="bio"><h4>Zahnärztin Sabine Hartung</h4>-2004 Studienabschluss<br>- von 2005 bis 2015 in England tätig<br>- Behandlungsschwerpunkte: ästhetische,<br>&nbsp;&nbsp;preventive Zahnheilkunde<br>&nbsp;&nbsp;Zahnaufhellung /Bleachingfeste,<br>&nbsp;&nbsp;kosmetische Zahnspangen<br>- Spezialgebiete: Wurzelkanalbehandlung<br>&nbsp;&nbsp;Endodontie,<br>&nbsp;&nbsp;seit 2009 Zahnfehlstellungskorrektur:<br>&nbsp;&nbsp;zertifizierte Aligner-Anbieterin</div></div>

<div class="abs member" style="left:143px;top:3659px"><div class="portrait" role="img" aria-label="Porträt der Zahnärztin"></div><div class="bio"><h4>Zahnärztin Sabine Hartung</h4>-2004 Studienabschluss<br>- von 2005 bis 2015 in England tätig<br>- Behandlungsschwerpunkte: ästhetische,<br>&nbsp;&nbsp;preventive Zahnheilkunde<br>&nbsp;&nbsp;Zahnaufhellung /Bleachingfeste,<br>&nbsp;&nbsp;kosmetische Zahnspangen<br>- Spezialgebiete: Wurzelkanalbehandlung<br>&nbsp;&nbsp;Endodontie,<br>&nbsp;&nbsp;seit 2009 Zahnfehlstellungskorrektur:<br>&nbsp;&nbsp;zertifizierte Aligner-Anbieterin</div></div>
<div class="abs member" style="left:611px;top:3659px"><div class="portrait" role="img" aria-label="Porträt der Stuhlassistentin"></div><div class="bio" style="padding-top:44px"><h4>Assistentin Olga Brandt</h4>- Stuhlassistentin<br>- allg. Bürotätigkeiten</div></div>

<div class="abs rule" style="left:6px;top:3865px;width:1194px"></div>

<h2 class="abs section-title" style="top:3902px;left:15px">Kontakt</h2>
<div class="abs contact" style="top:3996px">
  <p>Lindenweg 14</p>
  <p>09876 Grünwalde</p>
  <p style="margin-top:23px">Telefon: 03700-41520</p>
  <p>Fax: 03700-41529</p>
  <p style="margin-top:23px">E-Mail: info@zahnarzt-lindenhof.de</p>
  <p style="margin-top:23px">Unsere Öffnungszeiten:</p>
  <p style="margin-top:23px">Montag:&nbsp;&nbsp;&nbsp;&nbsp;&nbsp;&nbsp;9:00 bis 13:00 Uhr und 14:00 bis 19:00 Uhr</p>
  <p>Dienstag:&nbsp;&nbsp;&nbsp;&nbsp;9:00 bis 13:00 Uhr und 14:00 bis 19:00 Uhr</p>
  <p>Mittwoch:&nbsp;&nbsp;&nbsp;&nbsp;9:00 bis 14:00 Uhr</p>
  <p>Donnerstag: geschlossen</p>
  <p>Freitag:&nbsp;&nbsp;&nbsp;&nbsp;&nbsp;&nbsp;&nbsp;9:00 bis 13:00 Uhr</p>
  <p>... und nach Vereinbarung</p>
  <p class="blue" style="margin-top:44px">Telefonzeiten</p>
  <p class="blue" style="margin-top:23px">Innerhalb dieser Zeiten sind wir für Sie telefonisch erreichbar:</p>
  <p class="blue" style="margin-top:23px">Montag:&nbsp;&nbsp;&nbsp;&nbsp;&nbsp;&nbsp;9:00 bis 15:00 Uhr</p>
  <p class="blue">Dienstag:&nbsp;&nbsp;&nbsp;&nbsp;9:00 bis 15:00 Uhr</p>
  <p class="blue">Mittwoch:&nbsp;&nbsp;&nbsp;&nbsp;9:00 bis 12:00 Uhr</p>
  <p class="blue" style="margin-top:23px">In dringenden Fällen wenden Sie sich bitte an zahnärztlichen Notdienst.</p>
  <p class="blue" style="margin-top:23px">Link 'zur Notdienstsuche' https://www.zahnnotdienst-region.de/patienten/notdienstsuche/</p>
</div>

<div class="abs brand brand-foot"><span class="brand-dot" style="width:40px;height:40px"></span>Lindenhof Dental</div>
<div class="abs footer-box"></div>
<nav class="abs footer-nav"><span>Unsere Praxis</span><span>Leistungen</span><span>Praxislabor</span><span>Team</span><span>Kontakt</span></nav>
</body>
</html>
```